Business Cards for Branding (Advertising) Agency

We need stylish and cool business cards.
Additional info:
1) Logo - see the attachment. You can use either the three penguins or just one penguin face (square or round) - at your discretion.
2) Text and other stuff for business card:
front side:
-Logo and company name: company name - Northern Herons - should be in English as is in logo. This is the only exception. The rest of the text will be in Russian.
-Who we are: Брендинговое агентство
-First and last name:
-Position: Управляющий партнёр
-Address:
-Phone:
-Email:
-Website:
Note: please don't use names of information fields, such as: who we are, first and last name, position, address, phone, email and website.

3) Our suggestions on design:
-The backside of the business card can be either blank or has something on it - at your discretion.
-The business card background should be either white or grey (you can use any tone of grey).

Additional Information:
1) БРЕНДИНГОВОЕ АГЕНТСТВО
2) ул. Верескова - these two words should be together on the same line
3) тел.: +7 (495) 381-60-92
моб.: +7 (916) 507-28-14

Reason: We would like to receive more stylish designs.

```html
<!DOCTYPE html>
<html lang="ru">
<head>
<meta charset="utf-8">
<title>Northern Herons — визитные карточки</title>
<link rel="stylesheet" href="https://fonts.googleapis.com/css2?family=Open+Sans:wght@300;400;600;700&display=swap">
<style>
  :root {
    --backdrop: #d8d5d0;
    --card: #ffffff;
    --ink: #1a1a1a;
    --grey-text: #6f6f6f;
    --grey-line: #cfcfcf;
    --accent: #f39a1e;
  }
  * { box-sizing: border-box; margin: 0; padding: 0; }
  html, body { width: 1200px; height: 1000px; overflow: hidden; }
  body {
    background: var(--backdrop);
    font-family: "Open Sans", Arial, sans-serif;
    color: var(--ink);
    display: flex;
    flex-direction: column;
    align-items: center;
    justify-content: center;
    gap: 70px;
  }
  .card {
    width: 620px;
    height: 360px;
    background: var(--card);
    border-radius: 22px;
    box-shadow: 0 2px 0 #eee, 0 6px 0 #e4e4e4, 0 14px 26px rgba(0,0,0,.18);
    position: relative;
  }

  /* front */
  .card--front {
    display: flex;
    flex-direction: column;
    align-items: center;
    justify-content: center;
    gap: 22px;
  }
  .brand { display: flex; align-items: center; gap: 18px; }
  .brand__dot { width: 64px; height: 64px; border-radius: 50%; background: var(--ink); }
  .brand__name {
    font-size: 38px; font-weight: 400; letter-spacing: 6px;
    text-transform: uppercase; color: var(--ink); line-height: 1;
  }
  .brand--small .brand__dot { width: 30px; height: 30px; }
  .brand--small .brand__name { font-size: 18px; letter-spacing: 3px; }
  .tagline { color: var(--accent); font-size: 22px; font-weight: 300; }

  /* back */
  .card--back { padding: 40px 48px; }
  .card--back .brand { position: absolute; top: 40px; right: 48px; }
  .person { margin-top: 70px; border-top: 2px solid var(--grey-line); padding-top: 16px; width: 330px; }
  .person__name { color: var(--accent); font-size: 24px; font-weight: 600; }
  .person__role { color: var(--grey-text); font-size: 16px; font-weight: 700; margin-top: 2px; }
  .details { display: flex; margin-top: 26px; gap: 34px; }
  .contacts { list-style: none; display: flex; flex-direction: column; gap: 6px;
    padding-right: 34px; border-right: 2px dotted var(--grey-line); }
  .contacts li { display: flex; align-items: center; gap: 10px; font-size: 16px; font-weight: 300; color: var(--grey-text); }
  .icon { width: 20px; height: 20px; flex: none; }
  .address { font-size: 17px; font-weight: 300; color: var(--grey-text); line-height: 1.5; }
</style>
</head>
<body>
  <section class="card card--front" aria-label="Лицевая сторона визитки">
    <div class="brand">
      <span class="brand__dot"></span>
      <span class="brand__name">Northern Herons</span>
    </div>
    <p class="tagline">Брендинговое агентство</p>
  </section>

  <section class="card card--back" aria-label="Оборотная сторона визитки">
    <div class="brand brand--small">
      <span class="brand__dot"></span>
      <span class="brand__name">Northern Herons</span>
    </div>
    <div class="person">
      <p class="person__name">Мария Лебедева</p>
      <p class="person__role">Управляющий партнёр</p>
    </div>
    <div class="details">
      <ul class="contacts">
        <li>
          <svg class="icon" viewBox="0 0 20 20"><circle cx="10" cy="10" r="10" fill="var(--accent)"/><path d="M7 5.5l2 2-1 1.3c.6 1.3 1.6 2.3 2.9 2.9l1.3-1 2 2-1.2 1.6C9.8 14 6 10.2 5.3 6.7z" fill="#fff"/></svg>
          +7 (916) 507-28-14
        </li>
        <li>
          <svg class="icon" viewBox="0 0 20 20"><circle cx="10" cy="10" r="10" fill="var(--accent)"/><rect x="5" y="6.5" width="10" height="7" rx="1" fill="#fff"/><path d="M5.5 7l4.5 3.5L14.5 7" stroke="var(--accent)" stroke-width="1.2" fill="none"/></svg>
          maria@northernherons.ru
        </li>
        <li>
          <svg class="icon" viewBox="0 0 20 20"><circle cx="10" cy="10" r="10" fill="var(--accent)"/><circle cx="10" cy="10" r="5" fill="none" stroke="#fff" stroke-width="1.3"/><path d="M5 10h10M10 5c-2 3-2 7 0 10M10 5c2 3 2 7 0 10" stroke="#fff" stroke-width="1.1" fill="none"/></svg>
          www.northernherons.ru
        </li>
      </ul>
      <p class="address">117321, г. Москва<br>ул. Верескова, д.12, стр.2</p>
    </div>
  </section>
</body>
</html>
```